Organic Soap Packaging

We need a package design for a new company called Fern Naturals. Our primary product is organic soap. Our business model is based on the social entrepreneurial concept of by one give one like Valo shoes. We are giving soap to help prevent the spread of disease; 1.4 million deaths a year can be prevented by hand washing.

The design is for a recycled cardboard box/package. We want to demonstrate the high end, luxury feel of the product with undertones of organic/earth friendly/social conscious.

The soap is small batch, spa like, essential oil scented all natural luxury.
Updates

I am very excited about this startup business and I believe we will have great success! I am passionate about organic personal care and helping others in need. If you share my passion, please bring your work to the table!

Target Market(s)

My target market is people who are educated through college. Health conscious, socially conscious, Generation X. Basically shoppers of Green Basket and Halvorsen.

Industry/Entity Type

Business

Requirements
Must have
• Suitable for Face, Hair, and Skin
Scented with Organic Essential Oils

```html
<!DOCTYPE html>
<html lang="en">
<head>
<meta charset="utf-8">
<title>Fern Naturals – Soap Box Panel</title>
<link rel="stylesheet" href="https://fonts.googleapis.com/css2?family=Lobster+Two:ital,wght@0,700;1,700&display=swap">
<style>
  :root {
    --kraft: #c6a682;
    --kraft-light: #cfb08d;
    --kraft-dark: #b8966f;
    --ink: #3c3e3e;
    --leaf: #6a8a36;
    --leaf-light: #93b45a;
    --leaf-shadow: rgba(40, 45, 20, 0.55);
  }
  html, body {
    margin: 0;
    padding: 0;
    width: 1200px;
    height: 771px;
    overflow: hidden;
    background: var(--kraft);
  }
  .box-panel {
    position: relative;
    width: 1200px;
    height: 771px;
    background: radial-gradient(ellipse at 50% 45%, var(--kraft-light) 0%, var(--kraft) 60%, var(--kraft-dark) 100%);
    overflow: hidden;
  }
  .frame {
    position: absolute;
    inset: 0;
  }
  .corner-ornament {
    position: absolute;
    width: 150px;
    height: 150px;
    background: radial-gradient(circle at var(--cx) var(--cy), rgba(60, 62, 62, 0.38) 0%, rgba(60, 62, 62, 0.12) 55%, rgba(60, 62, 62, 0) 80%);
  }
  .corner-ornament.top-left { left: 32px; top: 29px; --cx: 0%; --cy: 0%; }
  .corner-ornament.top-right { right: 32px; top: 29px; --cx: 100%; --cy: 0%; }
  .corner-ornament.bottom-left { left: 32px; bottom: 30px; --cx: 0%; --cy: 100%; }
  .corner-ornament.bottom-right { right: 32px; bottom: 30px; --cx: 100%; --cy: 100%; }
  .edge-ornament {
    position: absolute;
    left: 430px;
    width: 340px;
    height: 36px;
    background: radial-gradient(ellipse at 50% 50%, rgba(60, 62, 62, 0.28) 0%, rgba(60, 62, 62, 0) 70%);
  }
  .edge-ornament.top { top: 42px; }
  .edge-ornament.bottom { bottom: 40px; }
  .brand {
    position: absolute;
    top: 312px;
    left: 0;
    width: 1200px;
    display: flex;
    align-items: center;
    justify-content: center;
    gap: 26px;
  }
  .brand-mark {
    width: 62px;
    height: 62px;
    background: var(--leaf-light);
  }
  .brand-name {
    font-family: "Lobster Two", cursive;
    font-weight: 700;
    font-style: normal;
    font-size: 100px;
    line-height: 1;
    color: var(--leaf);
    letter-spacing: 1px;
  }
  .claims {
    position: absolute;
    top: 494px;
    left: 0;
    width: 1200px;
    margin: 0;
    text-align: center;
    font-family: "Lobster Two", cursive;
    font-weight: 700;
    font-style: italic;
    font-size: 38px;
    line-height: 44px;
    letter-spacing: 1.5px;
    color: var(--leaf);
    text-shadow: 2px 2px 1px var(--leaf-shadow);
  }
  .claims span { display: block; }
</style>
</head>
<body>
  <main class="box-panel">
    <svg class="frame" width="1200" height="771" viewBox="0 0 1200 771" aria-hidden="true">
      <rect x="34" y="31" width="1132" height="709" fill="none" stroke="var(--ink)" stroke-width="3"/>
      <rect x="44" y="41" width="1112" height="689" fill="none" stroke="var(--ink)" stroke-width="1.5"/>
      <rect x="72" y="70" width="1056" height="632" fill="none" stroke="var(--ink)" stroke-width="2"/>
    </svg>
    <div class="corner-ornament top-left" role="img" aria-label="Scrollwork corner ornament"></div>
    <div class="corner-ornament top-right" role="img" aria-label="Scrollwork corner ornament"></div>
    <div class="corner-ornament bottom-left" role="img" aria-label="Scrollwork corner ornament"></div>
    <div class="corner-ornament bottom-right" role="img" aria-label="Scrollwork corner ornament"></div>
    <div class="edge-ornament top" role="img" aria-label="Scrollwork flourish along the top edge"></div>
    <div class="edge-ornament bottom" role="img" aria-label="Scrollwork flourish along the bottom edge"></div>

    <div class="brand">
      <div class="brand-mark"></div>
      <h1 class="brand-name">Fern Naturals</h1>
    </div>

    <p class="claims">
      <span>Suitable for Face, Hair, and Skin</span>
      <span>Scented with Organic Essential Oils</span>
    </p>
  </main>
</body>
</html>
```